Black Friday Sale Social Media Graphics

Focusing on Black Friday Graphics for each of the pics attached.  So need the product pics turned into  social media graphics (square size). For the color scheme of the graphics, they should all be complementary to the product colors.
You can add any of the stock photography attached but none are required. I mainly need BOLD text that says:
Black Friday Sale
Up to $15 Off
If you wanted to add smaller text, these headlines can work:
1.	Burn Belly Fat Fast!
2.	Double Your Weight Loss With Our Supplements!
3.	Lose Weight Naturally: Ditch the Prescription Pills & Needles!
4.	Tired of Stubborn Belly Fat? Discover What Works!
5.	Melt Away Belly Fat Faster with Our Supplements!
6.	Struggling to Lose Weight? Discover the Ultimate Solution!
7.	Ready to Burn Fat Faster?

Target Market(s)
women trying to lose weight
Industry/Entity Type
health and wellness
Requirements
Must have
- the product pics attached

Nice to have
- Bold text that says: Black Friday Sale

```html
<!DOCTYPE html>
<html lang="en">
<head>
<meta charset="UTF-8">
<title>Black Friday Supplements Promo</title>
<link rel="stylesheet" href="https://fonts.googleapis.com/css2?family=Anton&family=Montserrat:wght@300;800&display=swap">
<style>
  :root {
    --bg-black: #121112;
    --bg-deep: #1c1a1c;
    --promo-red: #d10a1c;
    --ink-black: #0a0a0a;
    --paper-white: #ffffff;
    --bottle-white: #eceef0;
    --bottle-shade: #b9bcc2;
  }
  html, body {
    margin: 0;
    padding: 0;
    width: 1200px;
    height: 1200px;
    overflow: hidden;
    background: var(--bg-black);
  }
  .promo-canvas {
    position: relative;
    width: 1200px;
    height: 1200px;
    overflow: hidden;
    background:
      radial-gradient(ellipse 520px 420px at 0% 0%, rgba(209,10,28,0.75), transparent 70%),
      radial-gradient(ellipse 700px 300px at 50% 100%, rgba(209,10,28,0.85), transparent 75%),
      radial-gradient(ellipse 380px 520px at 100% 55%, rgba(209,10,28,0.55), transparent 70%),
      radial-gradient(ellipse 600px 500px at 25% 55%, rgba(150,10,20,0.35), transparent 70%),
      linear-gradient(160deg, var(--bg-deep), var(--bg-black));
  }
  .offer-line {
    position: absolute;
    left: 0;
    top: 44px;
    width: 1200px;
    margin: 0;
    text-align: center;
    font-family: 'Montserrat', sans-serif;
    font-weight: 800;
    font-size: 38px;
    line-height: 1;
    letter-spacing: 6px;
    color: var(--paper-white);
  }
  .offer-line .offer-amount {
    color: var(--promo-red);
  }
  .headline-art {
    position: absolute;
    inset: 0;
  }
  .headline-word {
    font-family: 'Anton', 'Impact', sans-serif;
  }
  .product-lineup {
    position: absolute;
    left: 294px;
    top: 639px;
    width: 695px;
    height: 311px;
    border-radius: 22px;
    background: linear-gradient(180deg, var(--bottle-white) 0%, var(--bottle-shade) 100%);
  }
  .tagline {
    position: absolute;
    left: 0;
    width: 1200px;
    top: 976px;
    margin: 0;
    text-align: center;
    font-family: 'Montserrat', sans-serif;
    font-weight: 300;
    font-size: 36px;
    letter-spacing: 5px;
    color: var(--paper-white);
    line-height: 1;
  }
  .cta-bar {
    position: absolute;
    left: 222px;
    top: 1035px;
    width: 745px;
    height: 86px;
    background: var(--promo-red);
    clip-path: polygon(3% 0, 100% 0, 100% 100%, 0 100%);
    display: flex;
    align-items: center;
    justify-content: center;
  }
  .cta-text {
    margin: 0;
    font-family: 'Montserrat', sans-serif;
    font-weight: 800;
    font-size: 40px;
    letter-spacing: 4px;
    color: var(--paper-white);
  }
</style>
</head>
<body>
  <main class="promo-canvas">
    <p class="offer-line">SALE &middot; <span class="offer-amount">UP TO $15 OFF</span></p>

    <svg class="headline-art" width="1200" height="1200" viewBox="0 0 1200 1200">
      <defs>
        <linearGradient id="friday-fade" x1="0" y1="0" x2="0" y2="1">
          <stop offset="0" stop-color="#ffffff"/>
          <stop offset="0.75" stop-color="#ffffff"/>
          <stop offset="1" stop-color="#ffffff" stop-opacity="0.85"/>
        </linearGradient>
        <linearGradient id="flare-line" x1="0" y1="0" x2="1" y2="0">
          <stop offset="0" stop-color="#ff2a2a" stop-opacity="0"/>
          <stop offset="0.3" stop-color="#ff3b3b" stop-opacity="1"/>
          <stop offset="1" stop-color="#ff2a2a" stop-opacity="0"/>
        </linearGradient>
      </defs>
      <polygon class="title-band" points="261,117 1028,117 961,428 167,428" fill="#d10a1c"/>
      <rect class="flare" x="0" y="424" width="760" height="3" fill="url(#flare-line)"/>
      <rect class="flare" x="880" y="118" width="320" height="3" fill="url(#flare-line)"/>
      <text class="headline-word" x="269" y="394" textLength="750" lengthAdjust="spacingAndGlyphs"
            font-size="284" fill="#0a0a0a" transform="skewX(-10)">BLACK</text>
      <text class="headline-word" x="359" y="683" textLength="739" lengthAdjust="spacingAndGlyphs"
            font-size="284" fill="url(#friday-fade)" transform="skewX(-10)">FRIDAY</text>
    </svg>

    <div class="product-lineup" role="img" aria-label="Product photo: four white supplement bottles in a row with blue, green, red and pink labels"></div>

    <p class="tagline">DOUBLE YOUR WEIGHT LOSS</p>
    <div class="cta-bar">
      <p class="cta-text">WITH OUR SUPPLEMENTS!</p>
    </div>
  </main>
</body>
</html>
```